Website Design: Neuroscience research lab at an academic University.

I am looking to redo my University website for Neuroscience Research. <br/><br/>I am looking for a clean, modern and organized design to publish our work. Although I want a modern look, the focus should be on the text content.<br/><br/>Pages I need. These pages should be in the navigation bar;<br/>*Home*: with overview of the lab, contact information, and possibly with <br/>"Recent News and Events" information<br/>*Research*/Projects: will have text description, images, as well as video of various research projects we have done or are working on<br/>*People*: Personnel page with photos and bios of the team<br/>*Publications*: List of research articles with hyperlinks to online <br/>versions of articles as well as PDFs<br/>*News*: Continually updated list of events<br/><br/><br/>Some designs I like: <br/><br/>https://www.moravinlabs.example/<br/>http://www.quillbranch.example/<br/>https://tovernilab.example<br/>http://www.gradmerlab.example/<br/>https://vkot.halvern.example/

Target Market(s)

Academics, university students, government

Logo Text

Morvek Lab

Number of Pages Required

5+ page

Colors

Designer to choose colors to be used in the design.

Requirements
Must have
• A modern but elegant design that focuses on the research but that is also visually appealing.
• For the logo, please see the sketch in the attached files. That is a rough sketch of a logo that you can base your logo design on.
Should not have
• No search bar

```html
<!DOCTYPE html>
<html lang="en">
<head>
<meta charset="utf-8">
<title>Morvek Lab</title>
<link rel="stylesheet" href="https://fonts.googleapis.com/css2?family=Poppins:ital,wght@0,400;0,500;0,600;1,500&family=Abril+Fatface&display=swap">
<style>
:root{
  --red:#e8302a;
  --ink:#111111;
  --muted:#333333;
  --white:#ffffff;
  --card:#edf1f4;
  --footer:#000000;
  --rule:#2a2a2a;
}
*{margin:0;padding:0;box-sizing:border-box}
html,body{width:806px;height:1200px;overflow:hidden;background:var(--white);font-family:"Poppins",sans-serif;color:var(--ink)}
.page{position:relative;width:806px;height:1200px}
.abs{position:absolute}

.brand{left:157px;top:18px;display:flex;align-items:center;gap:6px}
.brand-dot{width:12px;height:12px;border-radius:50%;background:var(--red)}
.brand-name{font-weight:600;font-size:14px;color:var(--ink);letter-spacing:.2px}
.nav{top:23px;left:380px;display:flex;align-items:center;height:17px;font-size:7.5px}
.nav a{color:var(--ink);text-decoration:none;position:absolute;white-space:nowrap}
.nav .active{background:var(--red);color:var(--white);border-radius:9px;width:42px;height:17px;display:flex;align-items:center;justify-content:center;left:0}

.hero{left:0;top:58px;width:806px;height:252px;background:linear-gradient(180deg,#9dbde0 0%,#c9d9ea 30%,#a7b3bf 55%,#5a7040 80%,#6f9a3a 100%)}
.hero-title{left:0;top:160px;width:806px;text-align:center;font-family:"Abril Fatface",serif;font-size:23px;line-height:25px;color:var(--white);text-shadow:0 1px 3px rgba(0,0,0,.35)}
.hero-btn{left:354px;top:227px;width:98px;height:25px;border:1.5px solid var(--white);border-radius:13px;color:var(--white);font-weight:600;font-size:8px;display:flex;align-items:center;justify-content:center}
.arrow{top:173px;width:23px;height:22px;background:var(--white);display:flex;align-items:center;justify-content:center}
.dot-bar{left:378px;top:286px;width:15px;height:1.5px;background:var(--white)}

.intro-img{left:157px;top:353px;width:224px;height:169px;background:radial-gradient(ellipse 45% 42% at 50% 50%,#1f8a2a 0%,#136020 55%,#0a1a40 78%,#03041a 100%)}
.intro-title{left:409px;top:352px;width:240px;font-weight:600;font-size:9px;line-height:11px}
.intro-text{left:409px;top:381px;width:240px;font-size:6px;line-height:10px;color:var(--muted);text-align:justify}
.intro-text p+p{margin-top:10px}
.intro-btn{left:408px;top:494px;width:65px;height:22px;border:1.2px solid var(--red);border-radius:11px;color:var(--red);font-weight:600;font-size:5.5px;display:flex;align-items:center;justify-content:center}

.net{top:648px;width:195px;height:283px;background:radial-gradient(ellipse at 50% 80%,rgba(120,190,170,.18),rgba(230,120,100,.06) 60%,rgba(255,255,255,0) 80%)}
.news-heading{left:0;top:557px;width:806px;text-align:center;font-weight:600;font-size:13.5px}
.news-rule{left:388px;top:585px;width:29px;height:1px;background:var(--red)}
.paper{background:#f4f6f8;box-shadow:0 1px 4px rgba(0,0,0,.12)}
.card{left:226px;top:618px;width:346px;height:276px;background:var(--card);box-shadow:0 2px 6px rgba(0,0,0,.15)}
.scroll{left:560px;top:649px;width:3px;height:231px;background:#d5d9dd}
.scroll-thumb{left:559px;top:649px;width:4px;height:24px;background:var(--red);border-radius:2px}
.item{left:226px;width:346px}
.icon{position:absolute;left:20px;top:0;width:26px;height:26px;border:1px solid var(--red);border-radius:50%;display:flex;align-items:center;justify-content:center}
.item-body{position:absolute;left:57px;top:0;width:251px;font-size:5.9px;line-height:10px}
.item-date{color:var(--muted)}
.item-text{font-weight:500;text-align:justify;margin-top:2px}
.item-text em{font-style:italic}
.item-text u{text-decoration:underline}

.footer{left:0;top:931px;width:806px;height:269px;background:var(--footer)}
.f-brand{left:0;top:975px;width:806px;display:flex;justify-content:center;align-items:center;gap:6px}
.f-brand .brand-name{color:var(--white)}
.f-address{left:0;top:1029px;width:806px;text-align:center;color:var(--white);font-weight:500;font-size:7px;line-height:12px;font-style:normal}
.f-phone{left:0;width:806px;text-align:center;color:var(--white);font-size:10.5px}
.f-rule{left:157px;top:1147px;width:491px;height:1px;background:var(--rule)}
.f-copy{left:0;top:1168px;width:806px;text-align:center;color:#9a9a9a;font-size:7px}
</style>
</head>
<body>
<div class="page">

  <header>
    <div class="abs brand"><span class="brand-dot"></span><span class="brand-name">Morvek Lab</span></div>
    <nav class="abs nav">
      <a class="active" href="#">Home</a>
      <a href="#" style="left:49px">Research ⌄</a>
      <a href="#" style="left:104px">People</a>
      <a href="#" style="left:145px">Publications</a>
      <a href="#" style="left:204px">News</a>
      <a href="#" style="left:240px">Contact</a>
    </nav>
  </header>

  <section>
    <div class="abs hero" role="img" aria-label="Photograph of a modern glass-and-steel science building on campus, framed by trees and lawn under a blue sky"></div>
    <h1 class="abs hero-title">Learning, Memory and Decision<br>Making in the Mammalian Brain</h1>
    <div class="abs hero-btn">LEARN MORE</div>
    <div class="abs arrow" style="left:60px"><svg width="8" height="8" viewBox="0 0 8 8"><path d="M5.5 1 2.5 4 5.5 7" fill="none" stroke="#111" stroke-width="1"/></svg></div>
    <div class="abs arrow" style="left:718px"><svg width="8" height="8" viewBox="0 0 8 8"><path d="M2.5 1 5.5 4 2.5 7" fill="none" stroke="#111" stroke-width="1"/></svg></div>
    <div class="abs dot-bar"></div>
  </section>

  <section>
    <div class="abs intro-img" role="img" aria-label="Fluorescence microscopy image of a coronal rodent brain section glowing green on a dark background"></div>
    <h2 class="abs intro-title">Learning, Memory and Decision Making in the Mammalian Brain</h2>
    <div class="abs intro-text">
      <p>The Morvek Lab integrates behavior, electrophysiology, optogenetics and computational analysis to investigate the neural basis of learning, memory and decision making in the mammalian brain.</p>
      <p>The brain has a remarkable capacity to learn and to use past experience to guide our daily behavior. Multiple brain regions coordinate activity to form representations of the external world, learn new experiences, store and retrieve memories, and make decisions. We are interested in understanding the neural basis of these cognitive abilities by studying processing at the cellular and network level in neuronal circuits of the rodent brain.</p>
    </div>
    <div class="abs intro-btn">LEARN MORE</div>
  </section>

  <section>
    <div class="abs net" style="left:0" role="img" aria-label="Faint network-of-nodes decoration"></div>
    <div class="abs net" style="left:611px" role="img" aria-label="Faint network-of-nodes decoration"></div>
    <h2 class="abs news-heading">Recent News and Events</h2>
    <div class="abs news-rule"></div>

    <div class="abs paper" style="left:232px;top:610px;width:334px;height:292px"></div>
    <div class="abs paper" style="left:220px;top:626px;width:358px;height:260px"></div>
    <div class="abs card"></div>
    <div class="abs scroll"></div>
    <div class="abs scroll-thumb"></div>

    <div class="abs item" style="top:641px">
      <div class="icon"><svg width="12" height="12" viewBox="0 0 12 12" fill="none" stroke="#e8302a" stroke-width=".7"><rect x="2" y="1.5" width="8" height="9"/><path d="M3.5 4h5M3.5 6h5M3.5 8h5"/></svg></div>
      <div class="item-body"><div class="item-date">July 2019:</div><div class="item-text">NEW GRANT AWARD! Anvika receives the Harlow Trust Pathfinder Award.</div></div>
    </div>
    <div class="abs item" style="top:679px">
      <div class="icon"><svg width="12" height="12" viewBox="0 0 12 12" fill="none" stroke="#e8302a" stroke-width=".7"><rect x="2" y="1.5" width="8" height="9"/><path d="M3.5 4h5M3.5 6h5M3.5 8h5"/></svg></div>
      <div class="item-body"><div class="item-date">July 2019:</div><div class="item-text">NEW GRANT AWARD! The lab has received a 2nd R01 grant from NIRH!</div></div>
    </div>
    <div class="abs item" style="top:717px">
      <div class="icon"><svg width="12" height="12" viewBox="0 0 12 12" fill="none" stroke="#e8302a" stroke-width=".7"><rect x="2" y="1.5" width="8" height="9"/><path d="M3.5 4h5M3.5 6h5M3.5 8h5"/></svg></div>
      <div class="item-body"><div class="item-date">July 2019:</div><div class="item-text">Elias Brandt joins the lab as a postdoc. Welcome Eli!</div></div>
    </div>
    <div class="abs item" style="top:755px">
      <div class="icon"><svg width="12" height="12" viewBox="0 0 12 12" fill="none" stroke="#e8302a" stroke-width=".7"><rect x="2" y="1.5" width="8" height="9"/><path d="M3.5 4h5M3.5 6h5M3.5 8h5"/></svg></div>
      <div class="item-body"><div class="item-date">May 2019:</div><div class="item-text">New preprint in <u><em>preprintHub</em></u>, by graduate students Corin Vale and Lumi Haskel: <em>"Offline circuit reactivation supports route learning and choice"</em>.</div></div>
    </div>
    <div class="abs item" style="top:797px">
      <div class="icon"><svg width="12" height="12" viewBox="0 0 12 12" fill="none" stroke="#e8302a" stroke-width=".7"><rect x="2" y="1.5" width="8" height="9"/><path d="M3.5 4h5M3.5 6h5M3.5 8h5"/></svg></div>
      <div class="item-body"><div class="item-date">Apr 2019:</div><div class="item-text">New paper in <u><em>Journal of Neural Systems</em></u>, by graduate students Teodor Raske and Corin Vale: <em>"Rhythmic timing links spatial maps across distant memory and frontal circuits in behaving rodents"</em>.</div></div>
    </div>
    <div class="abs item" style="top:852px">
      <div class="icon"><svg width="12" height="12" viewBox="0 0 12 12" fill="none" stroke="#e8302a" stroke-width=".7"><rect x="2" y="1.5" width="8" height="9"/><path d="M3.5 4h5M3.5 6h5M3.5 8h5"/></svg></div>
      <div class="item-body"><div class="item-date">Feb 2019:</div><div class="item-text">News about our flavor mapping paper: <em>"Following the trail of every bite"</em>.</div></div>
    </div>
  </section>

  <footer>
    <div class="abs footer"></div>
    <div class="abs f-brand"><span class="brand-dot"></span><span class="brand-name">Morvek Lab</span></div>
    <address class="abs f-address">Callder 210<br>Ashbury University<br>88 Meridian Rd, MS-114,<br>Northvale MA 01990</address>
    <div class="abs f-phone" style="top:1083px">Lab: 555-014-2260</div>
    <div class="abs f-phone" style="top:1104px">Office: 555-014-2291</div>
    <div class="abs f-rule"></div>
    <div class="abs f-copy">Copyright © 2019 - Morvek Lab. All rights reserved.</div>
  </footer>

</div>
</body>
</html>
```